Podcast graphics

We are working on a launch of a podcast for couples in the fourth quarter of relationship.Our goal is to help couples in the 4th quarter of their life experience powerful and positive relationships. (Focus Age: 55-70) Maple Lantern may still be in career mode but beginning to wonder about retirement or "what's next" transitions. Some may choose conventional retirement or a transition to a different rhythm of life. These couples are active and have energy to work, volunteer, travel, and play. The focus is connecting resources and insights that will help them thrive in fourth quarter relationships. The Maple-Lantern podcast is the resource for an intentional dynamic couple life. Exploring physical and emotional health, travel, relationships, life after employment and much more.

Target Market(s)

couples in the 4th quarter of their life experience powerful and positive relationships. (Focus Age: 55-70)

Logo Text

open to concepts but text should identify the podcast as Maple lantern -

Requirements
Must have
• design specs in final artwork to meet podcast graphics standard of max 2048x2048
Nice to have
• high energy... the design will extend to a webpage for show notes and Chatterleaf page
Should not have
• not thinking something with an image of a couple but open to concepts.

```html
<!DOCTYPE html>
<html lang="en">
<head>
<meta charset="utf-8">
<title>Maple Lantern — Podcast Banner</title>
<link rel="stylesheet" href="https://fonts.googleapis.com/css2?family=Montserrat:wght@500;700&family=Playfair+Display:wght@700&display=swap">
<style>
  :root {
    --ember-deep: #5a0406;
    --ember-red: #b3100c;
    --ember-orange: #f0641a;
    --flare-yellow: #ffd21e;
    --word-dark: rgba(70, 0, 4, 0.72);
    --word-mid: rgba(150, 10, 12, 0.65);
    --word-light: rgba(255, 200, 190, 0.55);
    --word-yellow: #fff04a;
    --panel: rgba(28, 2, 4, 0.9);
    --cream: #fbe6b4;
  }
  html, body { margin: 0; padding: 0; overflow: hidden; background: #000; }
  .banner {
    position: relative;
    width: 1200px;
    height: 444px;
    overflow: hidden;
    font-family: "Montserrat", "Helvetica Neue", Arial, sans-serif;
    font-weight: 700;
  }
  .banner__texture {
    position: absolute; inset: 0;
    background:
      radial-gradient(ellipse 260px 220px at 90px 330px, var(--flare-yellow) 0%, var(--ember-orange) 35%, transparent 75%),
      radial-gradient(ellipse 380px 260px at 980px 180px, #e0361c 0%, transparent 70%),
      radial-gradient(ellipse 300px 200px at 420px 230px, #ff7a1e 0%, transparent 70%),
      linear-gradient(100deg, var(--ember-red) 0%, #d8281a 40%, #9e1010 65%, var(--ember-deep) 100%);
  }
  .word {
    position: absolute;
    margin: 0;
    white-space: nowrap;
    line-height: 1;
    letter-spacing: 0.01em;
    text-transform: uppercase;
  }
  .word--top     { left: -14px; top: -28px; font-size: 118px; color: var(--word-dark); }
  .word--emotion { left: 20px; top: 100px; font-size: 120px; color: var(--word-mid); }
  .word--invest  { left: -4px; top: 172px; font-size: 84px; color: var(--word-dark); }
  .word--real    { right: 20px; top: 168px; font-size: 80px; color: var(--word-mid); }
  .word--estate  { right: -20px; top: 232px; font-size: 76px; color: var(--word-dark); }
  .word--travel  { left: -10px; top: 238px; font-size: 80px; color: var(--word-light); opacity: .55; }
  .word--rel     { left: 230px; top: 282px; font-size: 78px; color: var(--word-yellow); }
  .word--ships   { left: 760px; top: 282px; font-size: 78px; color: var(--word-light); }
  .word--retire  { left: -20px; top: 330px; font-size: 150px; color: var(--word-dark); letter-spacing: 0.04em; }
  .word--small-health { left: 438px; top: 14px; font-size: 24px; color: var(--word-light); }
  .word--small-rel    { left: 478px; top: 340px; font-size: 24px; color: var(--word-light); }
  .word--vertical {
    left: 428px; top: 40px; font-size: 26px; color: var(--word-light);
    transform-origin: left top; transform: rotate(90deg) translateY(-30px);
    font-weight: 500;
  }
  .word--vertical-right {
    left: 800px; top: 40px; font-size: 22px; color: var(--word-dark);
    transform-origin: left top; transform: rotate(90deg);
    font-weight: 500;
  }
  .flare {
    position: absolute; left: 0; top: 0; width: 1200px; height: 444px;
  }
  .brand-panel {
    position: absolute;
    left: 459px; top: 42px;
    width: 310px; height: 276px;
    background: var(--panel);
    display: flex; flex-direction: column; align-items: center; justify-content: center;
  }
  .brand-panel__name {
    margin: 0;
    font-family: "Playfair Display", Georgia, serif;
    font-weight: 700;
    color: var(--cream);
    text-transform: uppercase;
    text-align: center;
    line-height: 1.05;
    font-size: 56px;
    letter-spacing: 0.02em;
  }
</style>
</head>
<body>
  <div class="banner">
    <div class="banner__texture" role="img" aria-label="Abstract fiery red and orange light texture with glowing flares"></div>

    <p class="word word--top">Physical Health</p>
    <p class="word word--emotion">Emotions</p>
    <p class="word word--travel">Travel</p>
    <p class="word word--invest">Investments</p>
    <p class="word word--real">Real</p>
    <p class="word word--estate">Estate</p>
    <p class="word word--rel">Relationships</p>
    <p class="word word--retire">Retirement</p>
    <p class="word word--small-health">Physical Health</p>
    <p class="word word--small-rel">Relationships</p>
    <p class="word word--vertical">Retirement Work</p>
    <p class="word word--vertical-right">Emotions Health</p>

    <svg class="flare" viewBox="0 0 1200 444" aria-hidden="true">
      <path d="M420 0 C 400 120, 380 260, 420 444" fill="none" stroke="#e07aff" stroke-width="3" opacity=".7"/>
      <path d="M0 420 C 120 330, 200 260, 300 230" fill="none" stroke="#fff6a0" stroke-width="2" opacity=".8"/>
    </svg>

    <div class="brand-panel">
      <h1 class="brand-panel__name">Maple<br>Lantern</h1>
    </div>
  </div>
</body>
</html>
```